Modern corporate energy/fuel business need business card design

Business card required for company founder. Korvan Fuel Systems is a Australian based modern energy/fuel provider. We offer specialised solutions to businesses using fossil fuels through renewable energy solutions.

I would like one side with specific information (name, address etc)

The other side to be bold, professional company name & logo. Striking.

Target Market(s)

B2B. Transport, mining, councils, environmentalist,

Industry/Entity Type

Petroleum

Contact Information for Business Card

Name; Peter Morrow
Position; Director
Email; pmorrow@korvanfuel.com.au
Address; PO Box 347, Kellyville, NSW, 2155
Website; www.korvanfuel.com.au

Colors

Designer to choose colors to be used in the design.

Requirements
Must have
• Clean, easy to read, professional & strong theme
Should not have
• too many colours, busy layout,

```html
<!DOCTYPE html>
<html lang="en">
<head>
<meta charset="utf-8">
<title>Korvan Fuel Systems – Business Card</title>
<link rel="stylesheet" href="https://fonts.googleapis.com/css2?family=Lato:wght@400;700&family=Montserrat:wght@400;700&display=swap">
<style>
  :root {
    --backdrop: #2b2b2b;
    --card-dark: #121212;
    --card-light: #ffffff;
    --navy: #1f4e79;
    --steel: #8fb0cc;
    --orange: #f26a21;
    --text-grey: #2a3f55;
  }
  * { box-sizing: border-box; margin: 0; padding: 0; }
  html, body {
    width: 1200px; height: 900px; overflow: hidden;
    background: var(--backdrop);
  }
  .canvas { position: relative; width: 1200px; height: 900px; }
  .card {
    position: absolute; left: 280px; width: 640px; height: 391px;
    box-shadow: 0 10px 30px rgba(0,0,0,.5);
    overflow: hidden;
  }
  .card--front { top: 49px; background: var(--card-dark); }
  .card--back { top: 460px; background: var(--card-light); }

  .company-name {
    position: absolute; margin: 0;
    font-family: "Montserrat", sans-serif; font-weight: 700;
    text-transform: uppercase; line-height: 1; white-space: nowrap;
  }
  .card--front .company-name {
    left: 0; right: 0; top: 176px; text-align: center;
    font-size: 40px; letter-spacing: 5px; color: var(--steel);
  }
  .card--back .company-name {
    right: 52px; top: 186px;
    font-size: 22px; letter-spacing: 2px; color: var(--navy);
  }

  .holder { position: absolute; left: 70px; top: 52px; }
  .holder__name {
    font-family: "Montserrat", sans-serif; font-weight: 700; font-size: 24px;
    letter-spacing: 1.5px; color: var(--navy); text-transform: uppercase;
  }
  .holder__role {
    font-family: "Montserrat", sans-serif; font-weight: 400; font-size: 15px;
    letter-spacing: 1px; color: var(--orange); text-transform: uppercase; margin-top: 4px;
  }
  .divider { position: absolute; left: 70px; top: 126px; }

  .contact {
    position: absolute; left: 70px; top: 234px; list-style: none;
    font-family: "Lato", sans-serif; font-size: 17px; color: var(--text-grey);
  }
  .contact li { display: flex; align-items: center; gap: 12px; height: 27px; }
  .contact svg { width: 15px; height: 15px; flex: none; }

  .address {
    position: absolute; right: 52px; bottom: 58px;
    font-family: "Lato", sans-serif; font-size: 18px; color: var(--text-grey);
  }
  .band {
    position: absolute; left: 0; bottom: 0; width: 100%; height: 38px;
    background: var(--orange);
  }
</style>
</head>
<body>
<main class="canvas">

  <section class="card card--front" aria-label="Card front">
    <p class="company-name">Korvan Fuel Systems</p>
  </section>

  <section class="card card--back" aria-label="Card back">
    <div class="holder">
      <h1 class="holder__name">Peter Morrow</h1>
      <p class="holder__role">Director</p>
    </div>

    <svg class="divider" width="300" height="4" viewBox="0 0 300 4">
      <line x1="0" y1="2" x2="100" y2="2" stroke="var(--orange)" stroke-width="2.5"/>
      <line x1="100" y1="2" x2="300" y2="2" stroke="var(--navy)" stroke-width="1.2"/>
    </svg>

    <p class="company-name">Korvan Fuel Systems</p>

    <ul class="contact">
      <li>
        <svg viewBox="0 0 16 16" aria-hidden="true"><path d="M4 1.5c1 0 1.6 2.8 1.4 3.4L4.3 6c.8 1.8 2 3 3.7 3.8l1.1-1.1c.6-.2 3.4.4 3.4 1.4v2c0 .9-.8 1.4-1.6 1.3C5.8 12.8 3.2 10.2 2.6 5.1 2.5 4.3 3 3.5 3.9 3.5z" fill="var(--orange)"/></svg>
        00 0000 0000
      </li>
      <li>
        <svg viewBox="0 0 16 16" aria-hidden="true"><rect x="1" y="3" width="14" height="10" rx="1" fill="var(--orange)"/><path d="M1.5 3.8 8 9l6.5-5.2" stroke="#fff" stroke-width="1.2" fill="none"/></svg>
        pmorrow@korvanfuel.com.au
      </li>
      <li>
        <svg viewBox="0 0 16 16" aria-hidden="true" fill="none" stroke="var(--orange)" stroke-width="1.1"><circle cx="8" cy="8" r="6.5"/><ellipse cx="8" cy="8" rx="2.8" ry="6.5"/><line x1="1.5" y1="8" x2="14.5" y2="8"/><line x1="2.5" y1="4.5" x2="13.5" y2="4.5"/><line x1="2.5" y1="11.5" x2="13.5" y2="11.5"/></svg>
        www.korvanfuel.com.au
      </li>
    </ul>

    <p class="address">PO Box 347, Kellyville, NSW, 2155</p>
    <div class="band"></div>
  </section>

</main>
</body>
</html>
```